7th Annual Falcon Ridge Classic Flyer

Looking to design an updated eye catching flyer maybe with someone movement, sound, and color. Below is an attachment of the flyer I have used in the past. I need to add color, sound, and movement to the flyer. This is an advertisement for youth folk style wrestling. You may contact me directly at 252-381-4927 if you need additional information. I really like the colors music and movement in the video below.
https://www.vidloomer.com/watch?v=kQ7mTbLw2Ra

Target Market(s)

Youth Wrestling

Font styles to use
Serif

Colors
EB3D1F
EC4F4E
F09395
F8D3D4
FCEDEE

Requirements
Must have
• All information included on flyer.
Nice to have
• Color, sound, and movement

```html
<!DOCTYPE html>
<html lang="en">
<head>
<meta charset="utf-8">
<title>7th Annual Falcon Ridge Classic Flyer</title>
<link rel="stylesheet" href="https://fonts.googleapis.com/css2?family=DM+Serif+Display&family=Poppins:wght@400;500;600;700;800&family=Oswald:wght@600&display=swap">
<style>
:root{
  --backdrop:#a7b4b9;
  --ink:#000;
  --maroon:#4a0000;
  --brick:#a84a4a;
  --gold:#f7a21b;
  --white:#fff;
  --paper:#fff;
}
*{box-sizing:border-box;margin:0;padding:0}
html,body{width:1200px;height:1200px;overflow:hidden;background:var(--backdrop);font-family:"Poppins",sans-serif;color:var(--white)}
.page{position:absolute;top:245px;width:512px;height:719px;overflow:hidden;
  background:
    linear-gradient(180deg,rgba(0,0,0,0) 70%,rgba(74,0,0,.85) 100%),
    linear-gradient(90deg,var(--maroon) 0%,#000 22%,#000 78%,var(--maroon) 100%);}
.page-front{left:74px}
.page-back{left:621px}
.abs{position:absolute}
/* front */
.hero-photo{left:0;top:0;width:512px;height:181px;
  background:radial-gradient(ellipse at 50% 45%,#8c7a5a 0%,#4a3a2c 40%,rgba(20,0,0,.9) 80%),linear-gradient(180deg,#d8d4cf,#2a0b08);}
.edition-seven{left:62px;top:118px;font-family:"DM Serif Display",serif;font-size:250px;line-height:1;color:var(--gold);
  -webkit-text-stroke:2px #c2361b;transform:scaleX(.72);transform-origin:left top}
.edition-suffix{left:198px;top:150px;font-family:"DM Serif Display",serif;font-size:120px;line-height:1;color:var(--gold);letter-spacing:-3px;
  -webkit-text-stroke:2px #c2361b}
.edition-rule{left:317px;top:265px;width:84px;height:5px;border-top:1.5px solid var(--gold);border-bottom:1.5px solid var(--gold)}
.annual{left:150px;top:255px;font-family:"DM Serif Display",serif;font-size:84px;line-height:1;color:var(--white);letter-spacing:-1px;z-index:2}
.event-name{left:143px;top:352px;width:238px;height:23px;background:var(--brick);
  clip-path:polygon(4% 0,96% 0,100% 100%,0 100%);text-align:center;font-size:18px;line-height:23px;font-weight:500}
.event-date{left:99px;top:401px;width:312px;height:26px;background:var(--gold);color:var(--ink);
  clip-path:polygon(0 0,100% 0,97% 50%,100% 100%,0 100%,3% 50%);text-align:center;font-size:18px;font-weight:700;line-height:26px}
.venue{left:0;width:512px;top:436px;text-align:center;font-size:8.4px}
.session{left:0;width:512px;text-align:center;font-size:8.4px}
.session b{font-weight:700}
.wave{left:110px;top:471px}
.register{left:89px;top:508px;height:27px;width:334px}
.register-label{position:absolute;left:0;top:0;width:124px;height:27px;background:var(--gold);color:var(--ink);
  clip-path:polygon(0 0,94% 0,100% 50%,94% 100%,0 100%,6% 50%);font-size:15px;line-height:27px;padding-left:30px}
.register-url{position:absolute;left:121px;top:0;width:213px;height:27px;background:var(--paper);color:var(--ink);
  clip-path:polygon(0 0,100% 0,96% 50%,100% 100%,0 100%,6% 50%);font-size:15px;line-height:27px;padding-left:15px}
.ticket{top:562px;width:141px;height:63px;border-radius:4px;overflow:hidden;background:var(--paper)}
.ticket-side{position:absolute;left:0;top:0;width:42px;height:63px;background:var(--brick);clip-path:polygon(0 0,45% 0,100% 100%,0 100%)}
.ticket-side span{position:absolute;left:2px;bottom:3px;transform-origin:left bottom;transform:rotate(-90deg) translate(0,100%);
  font-size:7.5px;line-height:9px;white-space:nowrap;width:58px}
.ticket-price{position:absolute;left:40px;top:1px;width:101px;text-align:center;font-family:"Oswald",sans-serif;font-size:27px;line-height:32px;color:var(--brick)}
.ticket-price sup{font-size:12px;color:var(--gold);vertical-align:12px}
.ticket-deadline{position:absolute;left:38px;top:35px;width:103px;height:13px;background:var(--brick);font-size:6.2px;line-height:13px;text-align:center}
.ticket-time{position:absolute;left:40px;top:48px;width:101px;height:15px;background:var(--gold);color:var(--ink);font-size:7.5px;line-height:15px;text-align:center}
.limit{left:93px;top:642px;width:328px;height:24px;background:var(--paper);color:var(--ink);border-radius:3px;text-align:center;font-size:12.5px;font-weight:700;line-height:24px}
.fee-note{left:0;width:512px;top:676px;text-align:center;font-size:10.5px}
.fee-note strong{color:var(--gold);font-size:16px;font-weight:700}
/* back */
.section-title{left:52px;font-size:14px;font-weight:700}
.boys-row{left:52px;width:204px;display:flex;gap:1px}
.boys-row .age{width:71px;background:var(--brick);font-size:8.6px;font-weight:700;display:flex;align-items:center;justify-content:flex-end;padding-right:4px}
.boys-row .weights{flex:1;background:var(--paper);color:#444;font-size:5.8px;line-height:1.5;padding:0 6px;display:flex;align-items:center}
.medals-photo{left:291px;top:21px;width:169px;height:209px;
  background:linear-gradient(90deg,rgba(40,80,200,.55) 0 18%,transparent 18% 40%,rgba(220,60,40,.55) 40% 58%,transparent 58% 75%,rgba(235,230,215,.5) 75% 90%,transparent 90%),
  linear-gradient(180deg,transparent 65%,rgba(200,150,40,.6) 80%,transparent 100%)}
.girls-col{top:263px}
.girls-col .head{height:17px;background:var(--gold);color:var(--ink);font-size:9.5px;font-weight:700;text-align:center;line-height:17px;border-radius:2px}
.girls-col .body{margin-top:3px;height:44px;background:var(--paper);color:#555;font-size:6px;line-height:1.65;text-align:center;padding:5px 8px;border-radius:2px}
.weigh-row{left:52px;width:408px;height:14px;display:flex;gap:1px;font-size:9.5px;font-weight:700;line-height:14px}
.weigh-row .day{width:96px;background:var(--gold);color:var(--ink);padding-left:3px}
.weigh-row .hours{width:110px;background:var(--brick);padding-left:5px}
.weigh-row .note{flex:1;margin-left:1px;background:linear-gradient(90deg,#2a0b06,#5a2308);font-weight:400;font-size:7.5px;padding-left:5px}
.rules{left:52px;top:461px;width:232px;list-style:none}
.rules li{position:relative;padding-left:21px;font-size:7.4px;line-height:10px;margin-bottom:7.5px}
.rules svg{position:absolute;left:0;top:0}
.admission-tab{left:331px;top:456px;width:104px;height:23px;background:var(--brick);border-radius:3px;text-align:center;font-size:15.5px;line-height:24px;z-index:2}
.admission-box{left:306px;top:471px;width:153px;height:101px;border-radius:5px;overflow:hidden;background:var(--paper)}
.admission-price{height:73px;padding-top:4px;background:var(--gold);color:var(--ink);font-family:"Oswald",sans-serif;font-size:52px;line-height:74px;text-align:center;letter-spacing:-1px}
.admission-price sup{font-size:26px;vertical-align:22px}
.admission-unit{color:var(--ink);font-size:17px;text-align:center;line-height:26px}
.tab{left:142px;width:215px;height:17px;background:var(--brick);clip-path:polygon(5% 0,95% 0,100% 100%,0 100%);text-align:center;font-size:12.5px;line-height:18px}
.contact-bar{left:44px;top:611px;width:420px;height:28px;background:var(--paper);border-radius:4px;padding:2px}
.contact-bar .inner{height:24px;display:flex;align-items:center;color:var(--ink);font-size:14.5px;font-weight:700;white-space:nowrap}
.contact-bar .who{background:var(--gold);height:24px;line-height:24px;padding:0 7px 0 8px;border-radius:3px 0 0 3px}
.phone-icon{width:22px;height:22px;background:var(--ink);border-radius:4px;display:flex;align-items:center;justify-content:center;margin:0 4px 0 5px}
.hotel-bar{left:44px;top:666px;width:420px;height:22px;background:var(--paper);border-radius:3px;display:flex;justify-content:center;align-items:center;gap:7px;color:var(--ink);font-size:8.2px;font-weight:600;white-space:nowrap}
.hotel-bar .name{color:#b5272b}
.hotel-bar .sep{width:1px;height:12px;background:#777}
</style>
</head>
<body>

<section class="page page-front">
  <div class="abs hero-photo" role="img" aria-label="Photo of tournament trophies, plaques and medals laid out on a table"></div>
  <div class="abs edition-seven">7</div>
  <div class="abs edition-suffix">th</div>
  <div class="abs edition-rule"></div>
  <div class="abs annual">Annual</div>
  <div class="abs event-name">Falcon Ridge Classic</div>
  <div class="abs event-date">Saturday, January 25, 2025</div>
  <p class="abs venue">Brookhaven Event Center 418 Larkspur Ave Brookhaven, NC 27590</p>
  <p class="abs session" style="top:458px"><b>4U, 6U, 8U, 10U</b> – Wrestling Starts at 8:30 am</p>
  <svg class="abs wave" width="292" height="6" viewBox="0 0 292 6"><path d="M0 3 q3 -3 6 0 t6 0 t6 0 t6 0 t6 0 t6 0 t6 0 t6 0 t6 0 t6 0 t6 0 t6 0 t6 0 t6 0 t6 0 t6 0 t6 0 t6 0 t6 0 t6 0 t6 0 t6 0 t6 0 t6 0 t6 0 t6 0 t6 0 t6 0 t6 0 t6 0 t6 0 t6 0 t6 0 t6 0 t6 0 t6 0 t6 0 t6 0 t6 0 t6 0 t6 0 t6 0 t6 0 t6 0 t6 0 t6 0 t6 0 t6 0" fill="none" stroke="#f7a21b" stroke-width="1"/></svg>
  <p class="abs session" style="top:480px"><b>12U, Middle School, &amp; High School</b> – Wrestling Starts at 1:00 pm</p>
  <div class="abs register">
    <div class="register-label">Register @</div>
    <div class="register-url">www.matbracket.com</div>
  </div>

  <div class="abs ticket" style="left:37px">
    <div class="ticket-side"><span>Early<br>Registration</span></div>
    <div class="ticket-price"><sup>$</sup>30.00</div>
    <div class="ticket-deadline">Deadline is January 19, 2025</div>
    <div class="ticket-time">at 11:59PM</div>
  </div>
  <div class="abs ticket" style="left:185px">
    <div class="ticket-side"><span>Early<br>Registration</span></div>
    <div class="ticket-price"><sup>$</sup>30.00</div>
    <div class="ticket-deadline">Deadline is January 19, 2025</div>
    <div class="ticket-time">at 11:59PM</div>
  </div>
  <div class="abs ticket" style="left:333px">
    <div class="ticket-side"><span>Early<br>Registration</span></div>
    <div class="ticket-price"><sup>$</sup>30.00</div>
    <div class="ticket-deadline">Deadline is January 19, 2025</div>
    <div class="ticket-time">at 11:59PM</div>
  </div>

  <div class="abs limit">Registration is limited to the first 500 wrestlers</div>
  <p class="abs fee-note">Non-RVYWA Card Holders will pay an additional <strong>$5.00</strong> at weigh-ins.</p>
</section>

<section class="page page-back">
  <h2 class="abs section-title" style="top:32px">Boys Divisions</h2>
  <div class="abs boys-row" style="top:59px;height:10px"><div class="age">4 &amp; Under</div><div class="weights">30, 40, 50, HWT</div></div>
  <div class="abs boys-row" style="top:74px;height:10px"><div class="age">6 &amp; Under</div><div class="weights">36, 40, 44, 48, 52, 56, 60, HWT</div></div>
  <div class="abs boys-row" style="top:89px;height:21px"><div class="age">8 &amp; Under</div><div class="weights">40, 44, 48, 52, 56, 60, 64, 68,<br>72, 76, 80, 84, 88, 92, HWT</div></div>
  <div class="abs boys-row" style="top:114px;height:21px"><div class="age">10 &amp; Under</div><div class="weights">52, 56, 60, 64, 68, 72, 76, 80,<br>84, 88, 92, 96, 100, 110, HWT</div></div>
  <div class="abs boys-row" style="top:140px;height:20px"><div class="age">12 &amp; Under</div><div class="weights">64, 68, 72, 76, 80, 84, 88, 92, 96, 100,<br>105, 110, 115, 120, 130, 140, 160, HWT</div></div>
  <div class="abs boys-row" style="top:165px;height:21px"><div class="age">Middle School</div><div class="weights">72, 76, 80, 88, 92, 96, 100, 105, 110,<br>115, 120, 130, 140, 160, 210, HWT</div></div>
  <div class="abs boys-row" style="top:191px;height:21px"><div class="age">High School</div><div class="weights">106, 113, 120, 126, 132, 138, 144, 150,<br>157, 165, 175, 190, 215, HWT</div></div>

  <div class="abs medals-photo" role="img" aria-label="Photo of first, second and third place medals on blue, red and white ribbons"></div>

  <h2 class="abs section-title" style="top:238px">Girls&nbsp; Divisions</h2>
  <div class="abs girls-col" style="left:52px;width:121px"><div class="head">K-5</div><div class="body">36, 40, 44, 48, 52, 56, 60, 64,<br>68, 72, 76, 80, 84, 88, 92, 96,<br>100, 110, 120,HWT</div></div>
  <div class="abs girls-col" style="left:187px;width:130px"><div class="head">Middle School</div><div class="body">72, 76, 83, 90, 98, 106, 113, 120,<br>126, 132, 138, 145, 152, 160, 170,<br>182, 190, 220, HWT</div></div>
  <div class="abs girls-col" style="left:331px;width:129px"><div class="head">Women’s High School</div><div class="body">100, 107, 114, 120, 126, 132, 145,<br>152, 165, 185, HWT</div></div>

  <h2 class="abs section-title" style="top:354px">Weigh-ins</h2>
  <div class="abs weigh-row" style="top:380px"><div class="day">January 24, 2025</div><div class="hours">5:00 pm to 7:00 pm</div><div class="note">(Early Weigh-ins - $10 cash due at scale)</div></div>
  <div class="abs weigh-row" style="top:398px"><div class="day">January 25, 2025</div><div class="hours">6:00 am to 7:30 am</div><div class="note">(4U, 6U, 8U, 10U)</div></div>
  <div class="abs weigh-row" style="top:416px"><div class="day">January 25, 2025</div><div class="hours">11:00 am to 12:00 pm</div><div class="note">(12 &amp; Under, MS, &amp; High School)</div></div>

  <ul class="abs rules">
    <li><svg width="11" height="11" viewBox="0 0 11 11"><circle cx="5.5" cy="5.5" r="5.5" fill="#f7a21b"/><path d="M3 5.6l1.8 1.8L8 4" fill="none" stroke="#000" stroke-width="1.4"/></svg>Tenths are waived/dropped at weigh-ins. Satellite weigh-ins will not be allowed.</li>
    <li><svg width="11" height="11" viewBox="0 0 11 11"><circle cx="5.5" cy="5.5" r="5.5" fill="#f7a21b"/><path d="M3 5.6l1.8 1.8L8 4" fill="none" stroke="#000" stroke-width="1.4"/></svg>High School Divisions are given 2 lbs. growth allowance.</li>
    <li><svg width="11" height="11" viewBox="0 0 11 11"><circle cx="5.5" cy="5.5" r="5.5" fill="#f7a21b"/><path d="M3 5.6l1.8 1.8L8 4" fill="none" stroke="#000" stroke-width="1.4"/></svg>Custom medals will be given to the top 3 individual finishers in each bracket.</li>
    <li><svg width="11" height="11" viewBox="0 0 11 11"><circle cx="5.5" cy="5.5" r="5.5" fill="#f7a21b"/><path d="M3 5.6l1.8 1.8L8 4" fill="none" stroke="#000" stroke-width="1.4"/></svg>Custom Awards will be awarded to the top 4 teams. Referee decisions will be final.</li>
    <li><svg width="11" height="11" viewBox="0 0 11 11"><circle cx="5.5" cy="5.5" r="5.5" fill="#f7a21b"/><path d="M3 5.6l1.8 1.8L8 4" fill="none" stroke="#000" stroke-width="1.4"/></svg>Pine Creek Athletics is not responsible for accidents, injuries, or theft during the tournament.</li>
  </ul>

  <div class="abs admission-box">
    <div class="admission-price"><sup>$</sup>10.00</div>
    <div class="admission-unit">per person</div>
  </div>
  <div class="abs admission-tab">Admission</div>

  <div class="abs tab" style="top:593px">For More Information, contact</div>
  <div class="abs contact-bar">
    <div class="inner">
      <span class="who">Tournament Director Dale Porter:</span>
      <span class="phone-icon"><svg width="14" height="14" viewBox="0 0 24 24"><path fill="#fff" d="M6.6 10.8a15.1 15.1 0 0 0 6.6 6.6l2.2-2.2c.3-.3.7-.4 1-.2 1.1.4 2.3.6 3.6.6.6 0 1 .4 1 1V20c0 .6-.4 1-1 1C10.6 21 3 13.4 3 4c0-.6.4-1 1-1h3.5c.6 0 1 .4 1 1 0 1.3.2 2.5.6 3.6.1.3 0 .7-.2 1z"/></svg></span>
      <span>(252) 381-4927</span>
    </div>
  </div>

  <div class="abs tab" style="top:648px">Hotels Available On-Site</div>
  <div class="abs hotel-bar">
    <span><span class="name">Lakeview Suites</span> (252) 610-2231</span><span class="sep"></span>
    <span><span class="name">Cedar Lodge</span> (252) 610-4478</span><span class="sep"></span>
    <span><span class="name">Harbor Stay</span> (252) 610-5592</span>
  </div>
</section>

</body>
</html>
```